Environmentally conscious Waste Management Company requires business card

We Require a Business card for our environmentally conscious waste management company . The business card should have a very clean design. be double sided and incorporate our logo..
The card will need o have 9 lines for the contact details - that are
Name
Title
Business
Address Line 1
Address Line 2
Address Line 3
Phone
Mobile
Email

Industry/Entity Type

Waste Management

Font styles to use
Other font styles liked:
• Helvetica or similar

```html
<!DOCTYPE html>
<html lang="en">
<head>
<meta charset="utf-8">
<title>Greenloop Business Card</title>
<link rel="stylesheet" href="https://fonts.googleapis.com/css2?family=Inter:wght@400;600&display=swap">
<style>
  :root {
    --brand-green: #1cba33;
    --card-white: #f3f3f3;
    --ink: #2b2b2b;
    --page-bg: #e4e4e2;
    --shadow: rgba(0, 0, 0, 0.14);
  }
  * { box-sizing: border-box; margin: 0; padding: 0; }
  html, body {
    width: 1200px;
    height: 900px;
    overflow: hidden;
    background: var(--page-bg);
    font-family: "Inter", Helvetica, Arial, sans-serif;
  }
  .canvas {
    width: 1200px;
    height: 900px;
    display: flex;
    flex-direction: column;
    align-items: center;
    justify-content: center;
    gap: 40px;
  }
  .card {
    position: relative;
    width: 700px;
    height: 400px;
    box-shadow: 0 6px 18px var(--shadow);
  }
  .card--front { background: var(--brand-green); }
  .card--back { background: var(--card-white); }

  /* Brand: plain name with a small dot beside it */
  .brand {
    position: absolute;
    display: flex;
    align-items: center;
    gap: 12px;
  }
  .brand__dot {
    width: 14px;
    height: 14px;
    border-radius: 50%;
    flex: none;
  }
  .brand__name {
    font-weight: 400;
    font-size: 34px;
    letter-spacing: 0.5px;
    line-height: 1;
  }
  .card--front .brand { left: 50%; top: 50%; transform: translate(-50%, -50%); }
  .card--front .brand__dot { background: #fff; }
  .card--front .brand__name { color: #fff; }

  .card--back .brand { left: 80px; top: 124px; }
  .card--back .brand__dot { background: var(--brand-green); }
  .card--back .brand__name { color: var(--brand-green); }

  /* Contact block */
  .contact {
    position: absolute;
    left: 368px;
    top: 122px;
    color: var(--ink);
    font-size: 11px;
    letter-spacing: 2px;
    line-height: 1;
  }
  .contact__name {
    font-size: 17px;
    letter-spacing: 4px;
    font-weight: 400;
  }
  .contact__title {
    color: var(--brand-green);
    font-size: 11px;
    margin-top: 6px;
  }
  .contact__business {
    font-weight: 600;
    margin-top: 22px;
  }
  .contact__line { margin-top: 9px; }
  .contact__phones { margin-top: 18px; }
  .contact__row {
    display: flex;
    align-items: center;
    gap: 10px;
    margin-top: 9px;
  }
  .contact__icon { width: 11px; height: 11px; flex: none; }
  .contact__email { margin-top: 12px; margin-left: 21px; }
</style>
</head>
<body>
<main class="canvas">
  <section class="card card--front" aria-label="Card front">
    <div class="brand">
      <span class="brand__dot"></span>
      <span class="brand__name">greenloop</span>
    </div>
  </section>

  <section class="card card--back" aria-label="Card back">
    <div class="brand">
      <span class="brand__dot"></span>
      <span class="brand__name">greenloop</span>
    </div>

    <div class="contact">
      <p class="contact__name">Mara Quill</p>
      <p class="contact__title">Title</p>
      <p class="contact__business">Greenloop Waste, Pty Ltd</p>
      <p class="contact__line">Address Line 1</p>
      <p class="contact__line">Address Line 2</p>
      <p class="contact__line">Address Line 3</p>
      <div class="contact__phones">
        <p class="contact__row">
          <svg class="contact__icon" viewBox="0 0 12 12" aria-hidden="true">
            <path d="M2.5 1h2l1 3-1.3 1a6 6 0 0 0 2.8 2.8L8 6.5l3 1v2A1.5 1.5 0 0 1 9.5 11 8.5 8.5 0 0 1 1 2.5 1.5 1.5 0 0 1 2.5 1z" fill="var(--brand-green)"/>
          </svg>
          <span>999 999 9999</span>
        </p>
        <p class="contact__row">
          <svg class="contact__icon" viewBox="0 0 12 12" aria-hidden="true">
            <rect x="3" y="0.5" width="6" height="11" rx="1" fill="none" stroke="var(--brand-green)" stroke-width="1.2"/>
            <rect x="5" y="9" width="2" height="1" fill="var(--brand-green)"/>
          </svg>
          <span>999 999 9999</span>
        </p>
      </div>
      <p class="contact__email">mara@greenloop.com</p>
    </div>
  </section>
</main>
</body>
</html>
```